Poster Required for Cafe to promote Catering

I would like a Poster made to advertise that our business does catering.
On the poster we would like it to say:

Did you know that Sunny Ladle does Catering?
We offer Breakfast, Lunch, Morning and Afternoon Tea Options
Come instore to enquire

At the bottom of the flyer, can you please put the contact details:
Phone 0487 602 914
Email tam@sunnyladlecanteen.com

Poster Size A3

I have attached our logo and menu's so you can get a feel for what we like.

Target Market(s)

Hospital Staff: Doctors, Nurses, Admin

Industry/Entity Type

Hospitality

Requirements
Nice to have
• Some pictures of catering. Eg. Gourmet Sandwiches, Sliders
• You could check our instagram page for ideas on what we do..
• @snyladle_qld

```html
<!DOCTYPE html>
<html lang="en">
<head>
<meta charset="utf-8">
<title>Sunny Ladle Catering Poster</title>
<link href="https://fonts.googleapis.com/css2?family=League+Gothic&family=Roboto+Condensed:wght@700&family=Raleway:wght@300&display=swap" rel="stylesheet">
<style>
  :root {
    --board: #1f1f1f;
    --board-edge: #141414;
    --cream: #fff8c6;
    --lemon: #f8f19a;
    --lemon-soft: rgba(248, 241, 154, 0.55);
    --lemon-faint: rgba(248, 241, 154, 0.12);
    --logo-ink: #3a2f30;
  }
  html, body {
    margin: 0;
    padding: 0;
    overflow: hidden;
    background: var(--board-edge);
  }
  .poster {
    position: relative;
    width: 849px;
    height: 1200px;
    overflow: hidden;
    background: radial-gradient(ellipse at 50% 45%, #2a2a2a 0%, var(--board) 55%, var(--board-edge) 100%);
    font-family: "League Gothic", "Oswald", sans-serif;
  }
  .headline {
    position: absolute;
    left: 108px;
    margin: 0;
    color: var(--cream);
    font-weight: 400;
    font-size: 143px;
    line-height: 117px;
    text-transform: uppercase;
    white-space: nowrap;
    transform: scaleX(0.75);
    transform-origin: left top;
  }
  .headline--top { top: 113px; }
  .headline--bottom { top: 555px; line-height: 118px; }
  .headline .mark { font-size: 1.15em; line-height: 0; }
  .brand-tile {
    position: absolute;
    left: 105px;
    top: 350px;
    width: 213px;
    height: 187px;
    background: var(--lemon);
    display: flex;
    align-items: center;
    justify-content: center;
  }
  .brand-tile__name {
    font-size: 44px;
    letter-spacing: 2px;
    color: var(--logo-ink);
    text-transform: uppercase;
  }
  .offer {
    position: absolute;
    left: 112px;
    top: 787px;
    margin: 0;
    color: var(--lemon);
    font-family: "Roboto Condensed", "Arial Narrow", sans-serif;
    font-weight: 700;
    font-size: 24px;
    line-height: 35px;
    text-transform: uppercase;
  }
  .call-to-action {
    position: absolute;
    left: 110px;
    top: 894px;
    margin: 0;
    color: var(--cream);
    font-size: 80px;
    line-height: 68px;
    font-weight: 400;
    text-transform: uppercase;
    white-space: nowrap;
    transform: scaleX(0.83);
    transform-origin: left top;
  }
  .contact {
    position: absolute;
    left: 112px;
    margin: 0;
    color: var(--lemon);
    white-space: nowrap;
  }
  .contact--phone {
    top: 1040px;
    font-family: "Roboto Condensed", "Arial Narrow", sans-serif;
    font-weight: 700;
    font-size: 28px;
  }
  .contact--email {
    top: 1078px;
    font-family: "Raleway", "Helvetica", sans-serif;
    font-weight: 300;
    font-size: 28px;
    letter-spacing: 2.6px;
  }
  .ornament-vine {
    position: absolute;
    left: 365px;
    top: 118px;
    width: 392px;
    height: 775px;
  }
  .ornament-vine__crown {
    position: absolute;
    left: 0;
    top: 0;
    width: 392px;
    height: 190px;
    border-radius: 95px 95px 60px 95px;
    background: radial-gradient(ellipse at 68% 45%, var(--lemon-soft) 0%, var(--lemon-faint) 60%, rgba(248, 241, 154, 0) 85%);
  }
  .ornament-vine__trail {
    position: absolute;
    left: 280px;
    top: 170px;
    width: 110px;
    height: 605px;
    border-radius: 55px;
    background: linear-gradient(180deg, var(--lemon-soft) 0%, rgba(248, 241, 154, 0.35) 55%, var(--lemon-faint) 100%);
  }
  .ornament-cup {
    position: absolute;
    left: 555px;
    top: 940px;
    width: 175px;
    height: 115px;
    border-radius: 16px 16px 40px 40px;
    background: var(--lemon);
  }
</style>
</head>
<body>
  <main class="poster">
    <h1 class="headline headline--top">Did you<br>know</h1>

    <div class="brand-tile">
      <span class="brand-tile__name">Sunny Ladle</span>
    </div>

    <h2 class="headline headline--bottom">Does<br>catering<span class="mark">?</span></h2>

    <p class="offer">We offer breakfast,<br>lunch and morning and<br>afternoon tea options</p>

    <p class="call-to-action">Come in store<br>to enquire</p>

    <p class="contact contact--phone">Phone 0487 602 914</p>
    <p class="contact contact--email">email:tam@sunnyladlecanteen.com</p>

    <div class="ornament-vine" role="img" aria-label="Decorative flowing yellow vine with a knotwork loop and small leaves, curling across the top and trailing down the right side">
      <div class="ornament-vine__crown" aria-hidden="true"></div>
      <div class="ornament-vine__trail" aria-hidden="true"></div>
    </div>
    <div class="ornament-cup" role="img" aria-label="Yellow coffee cup illustration with a heart cut-out"></div>
  </main>
</body>
</html>
```